New Bicycle shop business card

Hi!
I'm looking for a business card for my new proffesional bike mechanics shop. This shop is only for fixing broken bikes and not selling bikes.
Peferbly a modern and sleek and modern design.
Colors: black, grey, red, white
Information:
Name: Rijwielwerkplaats Vanhoutem
Shop owner: Bart Vanhoutem & Sanne Maertens
Website: www.rijwielwerkplaats-vanhoutem.be
Email: info@rijwielwerkplaats-vanhoutem.be
Phone number: +32471902386
Street adres: Kerkweg 64
9970 Oostmoere
Slogan/shop information: Herstellingen van alle merken.
Logo: see files.
Target Market(s)
People who seek a mechanic to fix or upgrade their bikes.
Contact Information for Business Card
Information:
Website: info@rijwielwerkplaats-vanhoutem.be
9970 Oostmoere
Logo: see files.

```html
<!DOCTYPE html>
<html lang="nl">
<head>
<meta charset="utf-8">
<title>Rijwielwerkplaats Vanhoutem – visitekaartje</title>
<link rel="stylesheet" href="https://fonts.googleapis.com/css2?family=Lato:wght@400;700;900&display=swap">
<style>
  :root {
    --backdrop: #3b3b3d;
    --card-dark: #1c1210;
    --card-light: #ffffff;
    --brand-red: #e0293b;
    --ink: #1a1a1a;
    --grey: #a7a7a7;
  }
  * { box-sizing: border-box; margin: 0; padding: 0; }
  html, body {
    width: 1200px; height: 1200px; overflow: hidden;
    background: var(--backdrop);
    font-family: "Lato", sans-serif;
  }
  .stage {
    position: relative; width: 1200px; height: 1200px;
    display: flex; flex-direction: column; align-items: center; justify-content: center; gap: 48px;
  }
  .card {
    position: relative; width: 880px; height: 500px;
    box-shadow: 0 18px 40px rgba(0,0,0,.35);
  }
  .card--back {
    background: var(--card-dark);
    border-radius: 80px 0 80px 0;
    display: flex; flex-direction: column; align-items: center; justify-content: center;
  }
  .card--front {
    background: var(--card-light);
    border-radius: 0 80px 0 80px;
  }
  .brand {
    display: flex; align-items: center; gap: 18px;
  }
  .brand__dot {
    width: 34px; height: 34px; border-radius: 50%; background: var(--brand-red); flex: none;
  }
  .brand__name {
    font-weight: 900; text-transform: uppercase; letter-spacing: 2px; line-height: 1.1;
  }
  .card--back .brand__name { color: var(--brand-red); font-size: 40px; text-align: center; }
  .tagline {
    margin-top: 70px; color: var(--brand-red);
    font-size: 22px; letter-spacing: 1px; text-transform: uppercase;
  }
  .owners {
    position: absolute; left: 60px; top: 52px;
  }
  .owners__names {
    color: var(--brand-red); font-weight: 900; font-size: 26px; text-transform: uppercase; line-height: 1.1;
  }
  .owners__role { color: var(--ink); font-size: 20px; margin-top: 2px; }
  .card--front .brand {
    position: absolute; right: 60px; top: 170px; flex-direction: column; align-items: flex-end; gap: 14px;
  }
  .card--front .brand__name { color: var(--ink); font-size: 34px; text-align: right; }
  .contact {
    position: absolute; left: 60px; bottom: 60px; list-style: none;
    font-size: 21px; color: var(--ink); line-height: 1.3;
  }
  .contact li { display: flex; align-items: center; gap: 10px; }
  .contact svg { width: 18px; height: 18px; fill: var(--brand-red); flex: none; }
  .address {
    position: absolute; right: 60px; bottom: 50px; text-align: right;
    font-size: 23px; color: var(--ink); line-height: 1.25; font-style: normal;
  }
</style>
</head>
<body>
<main class="stage">
  <section class="card card--back">
    <div class="brand">
      <span class="brand__dot"></span>
      <span class="brand__name">Rijwielwerkplaats<br>Vanhoutem</span>
    </div>
    <p class="tagline">Herstellingen van alle merken</p>
  </section>

  <section class="card card--front">
    <div class="owners">
      <p class="owners__names">Bart Vanhoutem &amp;<br>Sanne Maertens</p>
      <p class="owners__role">Owner</p>
    </div>

    <div class="brand">
      <span class="brand__dot"></span>
      <span class="brand__name">Rijwielwerkplaats<br>Vanhoutem</span>
    </div>

    <ul class="contact">
      <li>
        <svg viewBox="0 0 24 24" aria-hidden="true"><path d="M6.6 10.8a15.1 15.1 0 0 0 6.6 6.6l2.2-2.2a1 1 0 0 1 1-.25 11.4 11.4 0 0 0 3.6.57 1 1 0 0 1 1 1V20a1 1 0 0 1-1 1A17 17 0 0 1 3 4a1 1 0 0 1 1-1h3.5a1 1 0 0 1 1 1c0 1.25.2 2.45.57 3.6a1 1 0 0 1-.25 1z"/></svg>
        +32471902386
      </li>
      <li>
        <svg viewBox="0 0 24 24" aria-hidden="true"><path d="M2 5h20v14H2z M2 5l10 8 10-8" /></svg>
        info@rijwielwerkplaats-vanhoutem.be
      </li>
      <li>
        <svg viewBox="0 0 24 24" aria-hidden="true"><circle cx="12" cy="12" r="10"/></svg>
        www.rijwielwerkplaats-vanhoutem.be
      </li>
    </ul>

    <address class="address">Kerkweg 64<br>9970 Oostmoere</address>
  </section>
</main>
</body>
</html>
```